Business Card Design

I need a business card for my rental business. The business is named:
Hire a Vorlatrike Brenmoor
www.hireavorlatrikebrenmoor.example
(555) 014-2937
This will be a business card that I will leave at other businesses as advertisement so it needs to have the name, website, and phone number.
Please feel free to be creative. This is a new business so I have no designs.
Thank you very much for your time and I look forward to receiving your designs
Target Market(s)
Local rental customers
Industry/Entity Type
Business
Contact Information for Business Card
Please check out my website:
Other font styles liked:
- anything creative
Colors
Designer to choose colors to be used in the design.
Requirements
Must have
- Business name, phone, website. Rentals available hourly or daily. Book online

```html
<!DOCTYPE html>
<html lang="en">
<head>
<meta charset="UTF-8">
<title>Hire a Vorlatrike Brenmoor — Business Card</title>
<link rel="stylesheet" href="https://fonts.googleapis.com/css2?family=Oswald:wght@500&family=Russo+One&display=swap">
<style>
  :root {
    --backdrop: #121212;
    --card: #1c1c1d;
    --card-edge: #232324;
    --title: #8c9398;
    --text: #a6a6a6;
    --rule: #8a8a8a;
  }
  * { margin: 0; padding: 0; box-sizing: border-box; }
  html, body {
    width: 1200px;
    height: 897px;
    overflow: hidden;
    background: var(--backdrop);
  }
  .canvas {
    position: relative;
    width: 1200px;
    height: 897px;
  }
  .card {
    position: absolute;
    left: 303px;
    width: 595px;
    height: 338px;
    background: linear-gradient(135deg, var(--card) 0%, var(--card-edge) 60%, var(--card) 100%);
    box-shadow: 0 6px 14px rgba(0, 0, 0, 0.55);
    text-align: center;
  }
  .card--front { top: 92px; }
  .card--back { top: 469px; }
  .brand-name {
    position: absolute;
    left: 0;
    right: 0;
    font-family: "Russo One", sans-serif;
    font-weight: 400;
    color: var(--title);
    text-transform: uppercase;
    white-space: nowrap;
  }
  .card--front .brand-name {
    top: 80px;
    font-size: 24px;
    letter-spacing: 1.5px;
  }
  .card--back .brand-name {
    top: 150px;
    font-size: 27px;
    letter-spacing: 1.5px;
  }
  .details {
    position: absolute;
    left: 0;
    right: 0;
    top: 146px;
    font-family: "Oswald", sans-serif;
    font-weight: 500;
    font-size: 17px;
    line-height: 23px;
    letter-spacing: 1px;
    color: var(--text);
    text-transform: uppercase;
  }
  .details__rule {
    width: 184px;
    height: 1px;
    margin: 10px auto 9px;
    background: var(--rule);
  }
</style>
</head>
<body>
<main class="canvas">
  <section class="card card--front" aria-label="Card front">
    <h1 class="brand-name">Hire a Vorlatrike Brenmoor</h1>
    <div class="details">
      <p class="details__phone">Phone: (555) 014-2937</p>
      <p class="details__web">www.hireavorlatrikebrenmoor.example</p>
      <div class="details__rule"></div>
      <p class="details__offer">Rentals available hourly or daily</p>
      <p class="details__cta">Book online</p>
    </div>
  </section>
  <section class="card card--back" aria-label="Card back">
    <h2 class="brand-name">Hire a Vorlatrike Brenmoor</h2>
  </section>
</main>
</body>
</html>
```